Brightwave Reach - Business Card

We need a business card for a Social Media Marketing company that specializes in online marketing for small businesses in Canada using common Social Media platforms such as Pictora, Kinloop, Glimmet & Chirpo.

I have uploaded a copy of our logo which I would like utilized in the business card. We would like the business card to be modern yet classy design.

Our website is www.brightwavereach.ca

Industry/Entity Type

Marketing

Contact Information for Business Card

Email: info@brightwavereach.ca
Website: www.brightwavereach.ca
Telephone: 604-392-5108

Colors

Designer to choose colors to be used in the design.

Requirements
Must have
• Social Media icons on reverse
• Please add some designs with color.

```html
<!DOCTYPE html>
<html lang="en">
<head>
<meta charset="utf-8">
<title>Brightwave Reach - Business Card</title>
<link rel="stylesheet" href="https://fonts.googleapis.com/css2?family=Oswald:wght@600&family=Open+Sans:wght@400;600;700&display=swap">
<style>
  :root {
    --backdrop: #2a2b2d;
    --slate: #4a4d51;
    --slate-deep: #44474b;
    --paper: #ffffff;
    --ink: #4a4d51;
    --muted: #8c8f93;
    --light: #f2f2f2;
  }
  * { box-sizing: border-box; margin: 0; padding: 0; }
  html, body {
    width: 1200px; height: 1000px; overflow: hidden;
    background: var(--backdrop);
    font-family: "Open Sans", Arial, sans-serif;
  }
  .stage { position: relative; width: 1200px; height: 1000px; }
  .card {
    position: absolute; width: 560px; height: 320px;
    border-radius: 26px; overflow: hidden;
    box-shadow: 0 14px 30px rgba(0,0,0,.45);
  }

  /* Reverse side */
  .card-back { left: 320px; top: 150px; background: var(--slate); }
  .brand-mark {
    position: absolute; left: 50%; top: 92px; transform: translateX(-50%);
    display: flex; align-items: center; gap: 14px;
  }
  .brand-square { width: 16px; height: 16px; background: var(--light); flex: none; }
  .brand-name {
    font-family: "Oswald", Impact, sans-serif; font-weight: 600;
    color: var(--light); text-transform: uppercase;
    font-size: 40px; line-height: 1; letter-spacing: 1px;
  }
  .social-list {
    position: absolute; left: 0; right: 0; bottom: 42px;
    display: flex; justify-content: center; gap: 16px;
    list-style: none;
    font-size: 12px; font-weight: 600; color: var(--light);
  }

  /* Front side */
  .card-front { left: 320px; top: 520px; background: var(--slate-deep); }
  .front-paper-top {
    position: absolute; left: 0; top: 0; width: 100%; height: 142px;
    background: var(--paper);
  }
  .front-paper-left {
    position: absolute; left: 0; top: 141px; width: 350px; height: 94px;
    background: var(--paper);
  }
  .holder { position: absolute; left: 34px; top: 160px; }
  .holder-name {
    font-family: "Oswald", Impact, sans-serif; font-weight: 600;
    font-size: 30px; line-height: 1; color: var(--ink);
    text-transform: uppercase; letter-spacing: 1px;
  }
  .holder-title {
    margin-top: 4px; font-size: 16px; font-weight: 700; color: var(--muted);
    letter-spacing: .5px;
  }
  .front-brand {
    position: absolute; right: 40px; top: 164px;
    display: flex; align-items: center; gap: 10px;
  }
  .front-brand .brand-square { width: 10px; height: 10px; }
  .front-brand .brand-name { font-size: 22px; }
  .contact-list {
    position: absolute; left: 30px; bottom: 12px;
    list-style: none; color: var(--light);
    font-size: 12.5px; line-height: 24px;
  }
  .contact-list li { display: flex; align-items: center; gap: 12px; }
  .contact-list svg { width: 12px; height: 12px; flex: none; }
  .contact-list strong { font-weight: 700; }
</style>
</head>
<body>
<main class="stage">

  <section class="card card-back" aria-label="Card reverse">
    <div class="brand-mark">
      <span class="brand-square"></span>
      <span class="brand-name">Brightwave<br>Reach</span>
    </div>
    <ul class="social-list">
      <li>Kinloop</li>
      <li>Chirpo</li>
      <li>Pictora</li>
      <li>Glimmet</li>
    </ul>
  </section>

  <section class="card card-front" aria-label="Card front">
    <div class="front-paper-top"></div>
    <div class="front-paper-left"></div>

    <div class="holder">
      <p class="holder-name">Marcel Hayes</p>
      <p class="holder-title">Precedent</p>
    </div>

    <div class="front-brand">
      <span class="brand-square"></span>
      <span class="brand-name">Brightwave<br>Reach</span>
    </div>

    <ul class="contact-list">
      <li>
        <svg viewBox="0 0 24 24" aria-hidden="true"><path fill="#f2f2f2" d="M6.6 10.8a15.1 15.1 0 0 0 6.6 6.6l2.2-2.2c.3-.3.7-.4 1-.2 1.1.4 2.3.6 3.6.6.6 0 1 .4 1 1V20c0 .6-.4 1-1 1A17 17 0 0 1 3 4c0-.6.4-1 1-1h3.5c.6 0 1 .4 1 1 0 1.3.2 2.5.6 3.6.1.3 0 .7-.2 1z"/></svg>
        <span>604-392-5108</span>
      </li>
      <li>
        <svg viewBox="0 0 24 24" aria-hidden="true"><rect x="2" y="5" width="20" height="14" rx="1" fill="#f2f2f2"/><path d="M3 6.5l9 7 9-7" fill="none" stroke="#44474b" stroke-width="2"/></svg>
        <span>info@brightwavereach.ca</span>
      </li>
      <li>
        <svg viewBox="0 0 24 24" aria-hidden="true"><circle cx="12" cy="12" r="10" fill="#f2f2f2"/><path d="M2 12h20M12 2c3 3 3 17 0 20M12 2c-3 3-3 17 0 20" stroke="#44474b" stroke-width="1.5" fill="none"/></svg>
        <span>www.<strong>brightwavereach</strong>.ca</span>
      </li>
    </ul>
  </section>

</main>
</body>
</html>
```